Business Card Design Project

Need a business card design for a new company called Brellmoor.

We help large data center customers optimize and transform their data centers.

We have't gotten a logo yet but are in the process of running a separate contest to do that here on ArtHive.

Will post the logo shortly.
Updates

Project Deadline Extended
Reason: Not sure why this came up as a deadline of November 3d. We just launched it today. Going to send an email to ArtHive

Just uploaded larger files of the logo

Target Market(s)

Our target customers of our business are organizations with large data centers looking at optimizing their current data centers, relocating or consolidating their data centers into new data centers.

Typically our buyer will be the CIO, CTO or CFO of the organization.

Industry/Entity Type

Business

Font styles to use
Sans Serif

Colors
3276b5
fece3e

Requirements
Nice to have
• Be readable by the business card reader.
Should not have
• Small type that can't be scanned or easily read
Odd shape or size

```html
<!DOCTYPE html>
<html lang="en">
<head>
<meta charset="utf-8">
<title>Brellmoor Business Card</title>
<link href="https://fonts.googleapis.com/css2?family=Arimo:wght@400;700&display=swap" rel="stylesheet">
<style>
  :root {
    --card-bg: #ffffff;
    --card-border: #c9c9c9;
    --brand-panel: #1f2326;
    --brand-blue: #2a8fc4;
    --accent-orange: #e07b2a;
    --text-dark: #231f20;
    --text-muted: #8a8a8a;
    --glow-peach: #f6d8c2;
    --glow-blue: #d6e7f4;
  }
  * { margin: 0; padding: 0; box-sizing: border-box; }
  html, body { width: 1200px; height: 677px; overflow: hidden; background: var(--card-bg); }
  .card {
    position: relative;
    width: 1200px;
    height: 677px;
    background: var(--card-bg);
    border: 1px solid var(--card-border);
    font-family: "Arimo", Arial, sans-serif;
    overflow: hidden;
  }
  .brand-panel {
    position: absolute;
    left: 0; top: 106px;
    width: 577px; height: 464px;
    background: var(--brand-panel);
    display: flex;
    align-items: center;
    justify-content: center;
    gap: 18px;
  }
  .brand-dot {
    width: 46px; height: 46px;
    border-radius: 50%;
    background: var(--accent-orange);
  }
  .brand-name {
    font-size: 64px;
    font-weight: 400;
    color: var(--brand-blue);
    letter-spacing: 0.5px;
  }
  .corner-glow {
    position: absolute;
    right: 0; bottom: 0;
    width: 360px; height: 320px;
    background: radial-gradient(ellipse at 60% 60%, var(--glow-peach) 0%, var(--glow-blue) 45%, rgba(255,255,255,0) 75%);
    opacity: 0.55;
  }
  .contact {
    position: absolute;
    left: 640px; top: 100px;
  }
  .person-name {
    font-size: 48px;
    font-weight: 700;
    color: var(--brand-blue);
    line-height: 50px;
  }
  .designation {
    font-size: 33px;
    color: var(--text-muted);
    line-height: 40px;
    margin-bottom: 24px;
  }
  .contact-list { list-style: none; }
  .contact-item {
    display: flex;
    align-items: flex-start;
    font-size: 39px;
    color: var(--text-dark);
    line-height: 46px;
    white-space: nowrap;
  }
  .contact-item.phone { margin-bottom: 10px; }
  .contact-item.mobile { margin-bottom: 12px; }
  .contact-item.email { margin-bottom: 14px; }
  .contact-icon {
    width: 40px; height: 46px;
    margin-right: 26px;
    flex-shrink: 0;
    fill: var(--accent-orange);
  }
</style>
</head>
<body>
  <div class="card">
    <div class="corner-glow" role="img" aria-label="Faint soft brand colour glow decoration"></div>

    <div class="brand-panel">
      <span class="brand-dot"></span>
      <span class="brand-name">Brellmoor</span>
    </div>

    <div class="contact">
      <h1 class="person-name">Person Name</h1>
      <p class="designation">Designation</p>
      <ul class="contact-list">
        <li class="contact-item phone">
          <svg class="contact-icon" viewBox="0 0 40 46" aria-hidden="true">
            <path d="M2 22c0-6 8-10 18-10s18 4 18 10l-7 3-3-5H12l-3 5z"/>
            <path d="M7 27l5-5h16l5 5v3H7z"/>
            <circle cx="20" cy="27" r="3.5" fill="#fff"/>
          </svg>
          <span>901 4127 6083</span>
        </li>
        <li class="contact-item mobile">
          <svg class="contact-icon" viewBox="0 0 40 46" aria-hidden="true">
            <rect x="10" y="6" width="20" height="34" rx="4"/>
            <rect x="13" y="11" width="14" height="21" fill="#fff"/>
            <circle cx="20" cy="36" r="1.8" fill="#fff"/>
          </svg>
          <span>802 5219 3746</span>
        </li>
        <li class="contact-item email">
          <svg class="contact-icon" viewBox="0 0 40 46" aria-hidden="true">
            <rect x="1" y="13" width="38" height="24" rx="2"/>
            <path d="M3 15l17 13 17-13" fill="none" stroke="#fff" stroke-width="2.5"/>
            <path d="M3 35l12-10M37 35L25 25" fill="none" stroke="#fff" stroke-width="2"/>
          </svg>
          <span>info@brellmoor.com</span>
        </li>
        <li class="contact-item address">
          <svg class="contact-icon" viewBox="0 0 40 46" aria-hidden="true">
            <path d="M20 4c-7 0-12 5-12 12 0 8 12 26 12 26s12-18 12-26c0-7-5-12-12-12z"/>
            <circle cx="20" cy="16" r="5" fill="#fff"/>
          </svg>
          <span>Address will come here<br>Address will come here<br>Address will come here</span>
        </li>
        <li class="contact-item web">
          <svg class="contact-icon" viewBox="0 0 40 46" aria-hidden="true">
            <circle cx="20" cy="23" r="15"/>
            <g fill="none" stroke="#fff" stroke-width="2">
              <ellipse cx="20" cy="23" rx="6" ry="14"/>
              <path d="M6 23h28M8 16h24M8 30h24M20 9v28"/>
            </g>
          </svg>
          <span>www.brellmoor.com</span>
        </li>
      </ul>
    </div>
  </div>
</body>
</html>
```